Business card design needed

We are a Custom Joinery and specialise in design, Manufacture and Installation of kitchens and cabinetry
We currently have a logo based on the northern star in red and black but are open to something that would look fresh and clean
Updates

Project Deadline Extended
Reason: Need a couple days to go through designs. Finding some designs that are great on front and others great on reverse. I would like to be able to comment and get the total look we are after.

Target Market(s)

30-50 year olds who are looking to renovate

Industry/Entity Type

Business

Contact Information for Business Card

Maple Crest Interiors
ABN 37 418 260 503
Carlo Whitby - Cabinetmaker/Designer Licence No. 581907K

Requirements
Nice to have
• Maybe a nice fresh modern kitchen picture

```html
<!DOCTYPE html>
<html lang="en">
<head>
<meta charset="utf-8">
<title>Maple Crest Interiors – Business Card</title>
<link rel="stylesheet" href="https://fonts.googleapis.com/css2?family=Lato:wght@400;700;900&display=swap">
<style>
  :root {
    --page-bg: #3a3a3a;
    --card-dark: #231f1e;
    --card-dark-2: #302b29;
    --brand-red: #c4161c;
    --text-light: #ffffff;
    --text-soft: #e6e2df;
    --photo-wood: #7a5233;
    --photo-stone: #b9b4a8;
    --photo-shadow: #3b2a1f;
  }
  * { margin: 0; padding: 0; box-sizing: border-box; }
  html, body {
    width: 1200px;
    height: 949px;
    overflow: hidden;
    background: var(--page-bg);
    font-family: "Lato", sans-serif;
  }
  .canvas {
    position: relative;
    width: 1200px;
    height: 949px;
  }
  .business-card {
    position: absolute;
    left: 345px;
    top: 64px;
    width: 510px;
    height: 820px;
    overflow: hidden;
    box-shadow: 0 14px 36px rgba(0,0,0,0.55);
    background: var(--card-dark);
  }
  .kitchen-photo {
    position: absolute;
    left: 0; top: 0;
    width: 100%;
    height: 540px;
    background:
      linear-gradient(180deg, var(--photo-shadow) 0%, var(--photo-wood) 14%, var(--photo-stone) 38%, #cfc9bb 52%, var(--photo-wood) 72%, #5a3a24 100%);
  }
  .brand-block {
    position: absolute;
    left: 44px;
    top: 170px;
  }
  .brand-name {
    display: flex;
    align-items: center;
    gap: 14px;
    font-weight: 900;
    font-size: 34px;
    line-height: 1.05;
    color: var(--brand-red);
    text-transform: uppercase;
  }
  .brand-mark {
    width: 30px;
    height: 30px;
    background: var(--brand-red);
    flex: none;
  }
  .brand-address {
    margin-top: 10px;
    margin-left: 44px;
    font-size: 17px;
    line-height: 1.25;
    color: var(--text-light);
  }
  .contact-band {
    position: absolute;
    left: 0;
    top: 540px;
    width: 100%;
    height: 280px;
    background: linear-gradient(180deg, var(--card-dark-2) 0%, var(--card-dark) 100%);
    padding: 66px 0 0 62px;
    color: var(--text-light);
  }
  .person-name {
    font-weight: 700;
    font-size: 36px;
    line-height: 1;
  }
  .person-role {
    margin-top: 6px;
    font-size: 20px;
    color: var(--brand-red);
  }
  .contact-list {
    list-style: none;
    margin-top: 12px;
    font-size: 22px;
    line-height: 1.4;
    color: var(--text-soft);
  }
  .contact-list .email {
    font-size: 17px;
    margin-top: 6px;
  }
</style>
</head>
<body>
<main class="canvas">
  <article class="business-card">
    <div class="kitchen-photo" role="img" aria-label="Photo of a modern kitchen with timber ceiling, breakfast bar with black stools and a round wooden table"></div>

    <div class="brand-block">
      <div class="brand-name"><span class="brand-mark"></span><span>Maple Crest<br>Interiors</span></div>
      <p class="brand-address">Unit 12 15-21 Harlow Rd<br>Kingsvale NSW 2790</p>
    </div>

    <section class="contact-band">
      <h1 class="person-name">Carlo Whitby</h1>
      <p class="person-role">Cabinetmaker/Designer</p>
      <ul class="contact-list">
        <li>Mobile Ph: 0412 555 019</li>
        <li>Phone/Fax: 9555 0148</li>
        <li class="email">maplecrest@example.com.au</li>
      </ul>
    </section>
  </article>
</main>
</body>
</html>
```